business card design - photography

I am a fine art photographer. I would like to approach galleries to exhibit my work and need a business card.

The card should convey creativity and simplicity.
I would like a double sided card.

Some options:
1. An all white card with raised or embossed text or design to create a tactile finish.
2. a white and dark grey design would also work well.
3. Would be great to use my name as part of the design but not essential.
4. My name and title on the front, other details on the back of card.

The final design should be simple, minimal, elegant and innovative.
Being minimal, it will be more about texture, text size and placement.

examples of designs I would prefer provided here:
http://layoutmuse.net/ideas/40-plain-and-graceful-calling-card-layouts

I'm also open to other designs that may be unusual and unique.

Love this:
http://www.snapvault.com/pics/morningverses/583017264
Updates

I have uploaded a psd file after playing around in photoshop with various fonts.  I like the font (which I downloaded from typeshelf.net called Arual) but the design probably needs some refining.  I hope this helps.  If you'd like me to change the format of the file, please let me know.

Marta

Target Market(s)

Art Gallery owners/administrators and customers.

Industry/Entity Type

Business

Requirements
Must have
• A unique look.

Matte, silky finish or heavy textured stock. Double-sided card.

Front:
my name
photography by

Back:
phone no
email
web address
Nice to have
• Letterpress
embrossed
Clean fonts
Should not have
• Do not use illustrations of cameras or lenses.
No frames around the card edge.

```html
<!DOCTYPE html>
<html lang="en">
<head>
<meta charset="utf-8">
<title>Marta Vellan Photography – Business Card</title>
<link rel="stylesheet" href="https://fonts.googleapis.com/css2?family=Cinzel:wght@600&family=Questrial&display=swap">
<style>
  :root {
    --backdrop: #d9d9d7;
    --card: #f4f4f1;
    --card-edge: #e6e6e2;
    --name-blue: #3b4fa6;
    --muted-grey: #6f6f6f;
    --ink: #3a3a3a;
  }
  * { margin: 0; padding: 0; box-sizing: border-box; }
  html, body {
    width: 1200px;
    height: 874px;
    overflow: hidden;
    background: var(--backdrop);
  }
  .canvas {
    position: relative;
    width: 1200px;
    height: 874px;
  }
  .card {
    position: absolute;
    width: 520px;
    height: 300px;
    background: linear-gradient(160deg, #f8f8f5 0%, var(--card) 60%, var(--card-edge) 100%);
    box-shadow: 0 10px 26px rgba(0, 0, 0, 0.22), 0 2px 4px rgba(0, 0, 0, 0.12);
  }
  .card--front { left: 600px; top: 120px; }
  .card--back  { left: 80px;  top: 450px; }

  .wordmark {
    position: absolute;
    display: flex;
    flex-direction: column;
    align-items: flex-end;
  }
  .wordmark__name {
    font-family: "Cinzel", serif;
    font-weight: 600;
    color: var(--name-blue);
    font-variant: small-caps;
    letter-spacing: 0.02em;
    line-height: 1;
    white-space: nowrap;
  }
  .wordmark__title {
    display: flex;
    align-items: center;
    gap: 5px;
    font-family: "Questrial", sans-serif;
    color: var(--muted-grey);
    letter-spacing: 0.06em;
    text-transform: uppercase;
    line-height: 1;
  }
  .wordmark__dot { flex: none; }

  .card--front .wordmark { left: 40px; top: 118px; }
  .card--front .wordmark__name { font-size: 54px; }
  .card--front .wordmark__title { font-size: 15px; margin-top: 2px; }

  .card--back .wordmark { left: 30px; bottom: 26px; }
  .card--back .wordmark__name { font-size: 30px; }
  .card--back .wordmark__title { font-size: 9px; margin-top: 2px; }

  .contact {
    position: absolute;
    right: 30px;
    bottom: 30px;
    list-style: none;
    font-family: "Questrial", sans-serif;
    font-size: 11px;
    color: var(--ink);
    letter-spacing: 0.06em;
    text-transform: uppercase;
    line-height: 1.65;
  }
  .contact__label { color: var(--muted-grey); }
</style>
</head>
<body>
<main class="canvas">

  <section class="card card--front" aria-label="Card front">
    <div class="wordmark">
      <span class="wordmark__name">Marta Vellan</span>
      <span class="wordmark__title">
        <svg class="wordmark__dot" width="8" height="8" viewBox="0 0 8 8" aria-hidden="true"><circle cx="4" cy="4" r="3" fill="var(--muted-grey)"/></svg>
        Photography
      </span>
    </div>
  </section>

  <section class="card card--back" aria-label="Card back">
    <div class="wordmark">
      <span class="wordmark__name">Marta Vellan</span>
      <span class="wordmark__title">
        <svg class="wordmark__dot" width="6" height="6" viewBox="0 0 6 6" aria-hidden="true"><circle cx="3" cy="3" r="2.2" fill="var(--muted-grey)"/></svg>
        Photography
      </span>
    </div>
    <ul class="contact">
      <li><span class="contact__label">Phone:</span> 0412 578 904</li>
      <li><span class="contact__label">Email:</span> mvellan@inboxmail.net</li>
      <li><span class="contact__label">Website:</span> www.martavellan.com</li>
    </ul>
  </section>

</main>
</body>
</html>
```